Hot optical boutique needs a very creative mag ad!

I need a magazine ad in the following size:
Full page trim size = 9” W x 10.875” H
(bleed size = 9.25” W x 11.125” H)

I attached my logo, and another ad which you can get my address, directions off of. I also attached various pictures you are to use.
The purpose of this ad is as follows: We are a high fashion store that just returned from our buying trip in Paris and want to give our customers a peek at what we bought for them.
The title could be: We got back from Paris and our 2016 collections have arrived!

Target Market(s)

Fashionistas!

Industry/Entity Type

Boutique

Font styles to use
Sans Serif

Requirements
Must have
• See in description.
Nice to have
Should not have

```html
<!DOCTYPE html>
<html lang="en">
<head>
<meta charset="utf-8">
<title>Marlowe Opticians – 2016 Collections Ad</title>
<link rel="stylesheet" href="https://fonts.googleapis.com/css2?family=Bebas+Neue&family=Kaushan+Script&family=Arimo:ital,wght@0,400;0,700;1,400&display=swap">
<style>
  :root {
    --ad-red: #e3243a;
    --ad-red-deep: #c81a2e;
    --ad-white: #ffffff;
    --ad-black: #111111;
    --stage: #e6e6e6;
  }
  * { box-sizing: border-box; margin: 0; padding: 0; }
  html, body { width: 1200px; height: 1200px; overflow: hidden; background: var(--stage); }
  .ad-page {
    position: absolute; left: 110px; top: 8px;
    width: 980px; height: 1184px;
    background: var(--ad-white);
    overflow: hidden;
    font-family: "Arimo", Arial, sans-serif;
  }
  .hero-band { position: absolute; left: 0; top: 0; width: 980px; height: 900px; }
  .headline {
    position: absolute; left: 0; top: 58px; width: 100%;
    text-align: center; color: var(--ad-white);
    font-family: "Bebas Neue", "Oswald", sans-serif;
    font-weight: 400;
    font-size: 78px; line-height: 0.92; letter-spacing: 0.5px;
  }
  .feature-frame {
    position: absolute; left: 60px; top: 215px; width: 860px; height: 330px;
    border-radius: 40px;
    background: radial-gradient(ellipse at center, #f0303f 0%, #c81a2e 70%, rgba(200,26,46,0) 100%);
  }
  .headline-finish {
    position: absolute; left: 0; top: 430px; width: 100%;
    text-align: center; color: var(--ad-white);
    font-family: "Kaushan Script", cursive;
    font-weight: 400;
    font-size: 190px; line-height: 1.1;
  }
  .divider-line { position: absolute; left: 290px; top: 700px; width: 400px; height: 30px; }
  .product-row { position: absolute; left: 0; top: 770px; width: 980px; height: 230px; }
  .product-circle {
    position: absolute; width: 200px; height: 200px; border-radius: 50%;
    background: var(--ad-white); border: 5px solid var(--ad-red);
    display: flex; align-items: center; justify-content: center;
  }
  .product-shot {
    width: 150px; height: 60px; border-radius: 26px;
    background: linear-gradient(90deg, #8a9bc0, #d9dde6);
  }
  .contact-block { position: absolute; left: 80px; top: 1012px; width: 500px; color: var(--ad-black); }
  .contact-phone { font-size: 58px; line-height: 1; letter-spacing: 1px; }
  .contact-hours { font-size: 19px; margin-top: 8px; }
  .contact-address { font-size: 17px; font-weight: 700; margin-top: 8px; }
  .contact-landmark { font-size: 16px; font-style: italic; margin-top: 4px; padding-left: 30px; }
  .brand-mark {
    position: absolute; right: 40px; top: 1080px;
    display: flex; align-items: center; gap: 12px;
  }
  .brand-dot { width: 32px; height: 32px; border-radius: 50%; background: var(--ad-red); flex: none; }
  .brand-name { color: var(--ad-red); font-size: 28px; text-transform: uppercase; letter-spacing: 1px; white-space: nowrap; }
</style>
</head>
<body>
<main class="ad-page">
  <svg class="hero-band" viewBox="0 0 980 900" aria-hidden="true">
    <path d="M0 0 H980 V780 Q490 895 0 780 Z" fill="var(--ad-red)"/>
    <path d="M0 780 Q490 895 980 780" fill="none" stroke="var(--ad-black)" stroke-width="9"/>
  </svg>

  <div class="feature-frame" role="img" aria-label="Photo of red shield sunglasses with thin black temples"></div>

  <h1 class="headline">We got back from Paris and<br>our 2016 collections have</h1>
  <p class="headline-finish">arrived</p>

  <svg class="divider-line" viewBox="0 0 400 30" aria-hidden="true">
    <path d="M0 18 Q200 8 400 4" fill="none" stroke="var(--ad-white)" stroke-width="4" stroke-linecap="round"/>
  </svg>

  <section class="product-row">
    <div class="product-circle" style="left:75px; top:20px;"><div class="product-shot" role="img" aria-label="Aviator sunglasses with blue lenses"></div></div>
    <div class="product-circle" style="left:285px; top:28px;"><div class="product-shot" role="img" aria-label="Gold aviator sunglasses with brown lenses" style="background:linear-gradient(90deg,#b29a7c,#ece4d8)"></div></div>
    <div class="product-circle" style="left:495px; top:22px;"><div class="product-shot" role="img" aria-label="Shield sunglasses with grey gradient lens" style="background:linear-gradient(180deg,#3a3f4a,#e7e9ee)"></div></div>
    <div class="product-circle" style="left:705px; top:0px;"><div class="product-shot" role="img" aria-label="Blue rectangular optical frames" style="background:linear-gradient(90deg,#2f7fb0,#cfe6f2)"></div></div>
  </section>

  <section class="contact-block">
    <p class="contact-phone">555.214.7730</p>
    <p class="contact-hours">OPEN MON-WED 10-6 • THUR-SAT 10-9</p>
    <p class="contact-address">SHOPS AT LINDEN PLAZA ON HARBOR ROAD</p>
    <p class="contact-landmark">Next to Casa Verde Tacos and Olive Grill</p>
  </section>

  <div class="brand-mark">
    <span class="brand-dot"></span>
    <span class="brand-name">Marlowe Opticians</span>
  </div>
</main>
</body>
</html>
```